Tildens Biscuit Barn Website

I need a website for a diner/restaurant that has been established in a farming, oil and industrial community for over 15 years. The website needs to be simple in design, but that should demonstrate the mastery of skills of the designer. Our diner/restaurant is family oriented, patriotic but very rustic
Fb Address is fb.me/TildensBarn

Pictures of the restaurant

https://www.filecrate-example.net/s/qk72hdw01/Tildens_05.jpg

Pictures of About us

https://www.filecrate-example.net/sh/zm40vrt88/AboutUsPhotos

Article about Tilden's
https://www.filecrate-example.net/s/wp31nbx57/TildensBiscuitBarn1.PDF
https://www.filecrate-example.net/s/hy65lcu29/TildensBiscuitBarn2.PDF

Reason: I was slow to update with information.

Reason: I am just getting feedback to the designs posted. I wasn't sure of the limited feedback was limiting designers from submitting designs. That and running a business with 25 employees open 12 hours a day, being here 2 hours prior and 2-3 hours after makes for long days.

I've increased the first place prize and also added funds to the second and third place prizes for your effort.

I just need the files in PSD, not HTML 5 as originally requested. We can handle getting the coding part.

Ill have the contest finalized by Monday. Thanks for your patience.

Target Market(s)

Cross section of adults from 18-35 & 35-55.

Industry/Entity Type

Industrial

Font styles to use
Other font styles liked:
• ff tisa web pro or garamond premier pro

Requirements
Must have
• Must be clean, look nice and not look like an afterthought.
Nice to have
• Please see the last two documents for information about our restaurant, which was featured in our local newspaper.

```html
<!DOCTYPE html>
<html lang="en">
<head>
<meta charset="utf-8">
<title>Tilden's Biscuit Barn</title>
<link rel="stylesheet" href="https://fonts.googleapis.com/css2?family=Arimo:wght@400;700&family=Dancing+Script:wght@700&family=Fira+Sans:ital,wght@0,800;1,800&family=Oswald:wght@500&display=swap">
<style>
:root{
  --red:#d7000f;
  --yellow:#ffd100;
  --ink:#231f20;
  --text:#222;
  --grey-bg:#ececec;
  --pale:#fafafa;
  --footer-nav:#6c6c6c;
  --footer:#5e5e5e;
  --line:#d4d4d4;
  --social:#4a90d9;
}
*{margin:0;padding:0;box-sizing:border-box}
html,body{width:1200px;height:1125px;overflow:hidden}
body{position:relative;background:var(--pale);font-family:"Arimo",Arial,sans-serif;color:var(--text)}
a{color:inherit;text-decoration:none}

.backdrop{position:absolute;left:0;top:0;width:1200px;height:815px;background:linear-gradient(#f7f7f7 0,#e9e9e9 60%,var(--grey-bg) 100%)}

.site-header{position:absolute;left:0;top:0;width:1200px;height:100px;background:#fff;border-bottom:3px solid var(--red)}
.nav-main{position:absolute;top:62px;display:flex;gap:18px;font-family:"Dancing Script",cursive;font-size:22px;color:var(--ink)}
.nav-main a{padding:0 18px;height:32px;line-height:32px;border-radius:6px}
.nav-main a.is-active{background:var(--red);color:#fff}
.nav-left{left:134px}
.nav-right{left:735px}
.brand{position:absolute;left:472px;top:0;width:243px;height:112px;background:#fff;display:flex;align-items:center;justify-content:center;gap:8px}
.brand-mark{width:14px;height:14px;border-radius:50%;background:var(--red)}
.brand-name{font-family:"Oswald",sans-serif;font-size:25px;line-height:1.05;color:var(--red);text-align:left}
.social{position:absolute;display:flex;align-items:center;gap:8px;font-size:12px;color:#888}
.social i{width:24px;height:24px;border-radius:50%;background:var(--social);display:block}
.social-top{right:108px;top:5px}

.hero{position:absolute;left:0;top:0}

.block-title{position:absolute;top:550px;display:flex;align-items:center;gap:8px;font-family:"Oswald",sans-serif;font-size:23px;color:var(--red)}
.hours-title{left:100px}
.location-title{right:102px}

.hours{position:absolute;left:100px;top:597px;width:276px;border-collapse:collapse;font-size:12px;font-weight:700}
.hours td{height:21px;border-top:1px solid var(--line);padding-top:3px}
.hours tr:last-child td{border-bottom:1px solid var(--line)}
.hours td:first-child{padding-left:44px}

.newsletter{position:absolute;left:394px;top:596px;width:414px;height:87px;background:var(--ink);border-radius:8px;padding:12px 23px}
.newsletter h3{font-family:"Fira Sans",sans-serif;font-weight:800;font-size:20px;color:#fff;margin-bottom:4px;letter-spacing:.2px}
.newsletter-row{display:flex;gap:7px}
.newsletter input{width:308px;height:31px;border:0;border-radius:5px;padding:0 14px;font:12px "Arimo",sans-serif;color:#999}
.newsletter button{width:58px;height:31px;border:0;border-radius:5px;background:var(--yellow);font-family:"Fira Sans",sans-serif;font-weight:800;font-size:19px;color:var(--ink)}

.location{position:absolute;left:824px;top:597px;width:276px;height:86px;border-top:1px solid var(--line);border-bottom:1px solid var(--line);text-align:right;padding:9px 53px 0 0;font-size:11px;font-weight:700;line-height:17px}
.location a{color:var(--red);font-weight:400;text-decoration:underline}

.dishes{position:absolute;left:0;top:738px;width:1200px}
.dish{position:absolute;width:190px;text-align:center}
.dish-photo{display:block;width:160px;height:160px;margin:0 auto;border-radius:50%;border:3px solid #fff;box-shadow:0 2px 6px rgba(0,0,0,.15)}
.dish h4{font-family:"Oswald",sans-serif;font-weight:500;font-size:18px;color:var(--ink);margin-top:12px;line-height:24px}
.dish p{font-size:12px;color:#333}

.footer-nav{position:absolute;left:0;top:968px;width:1200px;height:45px;background:var(--footer-nav);border-top:2px solid #444;border-bottom:1px solid #7a7a7a;display:flex;justify-content:center;align-items:center;font-size:12.5px;color:#fff}
.footer-nav a+a::before{content:"|";color:var(--yellow);margin:0 22px}
.site-footer{position:absolute;left:0;top:1013px;width:1200px;height:112px;background:var(--footer);color:#fff}
.footer-brand{position:absolute;left:102px;top:33px;display:flex;align-items:center;gap:8px}
.footer-brand .brand-mark{background:#cfcfcf}
.footer-brand .brand-name{color:#cfcfcf;font-size:20px}
.footer-info{position:absolute;left:270px;top:36px;font-size:11px;line-height:18px}
.footer-info strong{font-size:12px}
.social-bottom{right:90px;top:40px;color:#fff}
.copyright{position:absolute;right:100px;top:73px;font-size:11px}
</style>
</head>
<body>
<div class="backdrop"></div>

<svg class="hero" width="1200" height="600" viewBox="0 0 1200 600">
  <defs>
    <clipPath id="hero-disc"><circle cx="600" cy="85" r="493"/></clipPath>
    <linearGradient id="photo-tone" x1="0" y1="0" x2="1" y2="1">
      <stop offset="0" stop-color="#f2eeea"/>
      <stop offset=".45" stop-color="#8a6a4c"/>
      <stop offset="1" stop-color="#c27a2c"/>
    </linearGradient>
    <filter id="disc-shadow" x="-10%" y="-10%" width="120%" height="130%">
      <feDropShadow dx="0" dy="2" stdDeviation="3" flood-opacity=".18"/>
    </filter>
  </defs>
  <circle cx="600" cy="85" r="500" fill="#fff" filter="url(#disc-shadow)"/>
  <g clip-path="url(#hero-disc)">
    <rect x="100" y="100" width="1000" height="400" fill="#f6f6f6"/>
    <rect x="300" y="150" width="580" height="348" fill="url(#photo-tone)" role="img" aria-label="Glass of black coffee with a croissant and layered cake"/>
    <rect x="100" y="498" width="1000" height="100" fill="var(--red)"/>
  </g>
  <circle cx="812" cy="481" r="5" fill="var(--yellow)"/>
  <circle cx="830" cy="481" r="5" fill="var(--yellow)"/>
  <circle cx="849" cy="481" r="5" fill="var(--red)"/>
  <circle cx="867" cy="481" r="5" fill="var(--yellow)"/>
  <g transform="translate(843 248) rotate(-18)">
    <polygon fill="var(--yellow)" points="0,-66 10,-54 22,-62 27,-48 41,-51 40,-37 54,-34 47,-22 60,-14 49,-4 58,8 45,14 50,28 36,30 36,44 22,43 17,57 5,50 -4,62 -12,51 -24,58 -27,44 -41,46 -39,32 -53,28 -45,16 -58,8 -48,-2 -57,-14 -44,-20 -48,-34 -34,-35 -34,-50 -20,-48 -14,-61 -3,-53"/>
    <text x="0" y="-10" text-anchor="middle" font-family="Fira Sans, sans-serif" font-weight="800" font-size="22" fill="var(--red)">ORDER</text>
    <text x="0" y="12" text-anchor="middle" font-family="Fira Sans, sans-serif" font-weight="800" font-size="22" fill="var(--red)">ONLINE</text>
    <text x="0" y="28" text-anchor="middle" font-family="Fira Sans, sans-serif" font-weight="800" font-size="11" fill="var(--ink)">CLICK HERE</text>
  </g>
  <text x="603" y="522" text-anchor="middle" font-family="Fira Sans, sans-serif" font-weight="800" font-size="20" fill="var(--yellow)">place your order now!</text>
  <text x="603" y="556" text-anchor="middle" font-family="Fira Sans, sans-serif" font-style="italic" font-weight="800" font-size="38" fill="#fff">555 014 2273</text>
</svg>

<header class="site-header">
  <nav class="nav-main nav-left"><a class="is-active" href="#">Home</a><a href="#">Menu</a><a href="#">Order online</a></nav>
  <a class="brand" href="#"><span class="brand-mark"></span><span class="brand-name">Tilden's<br>Biscuit Barn</span></a>
  <nav class="nav-main nav-right"><a href="#">Reservations</a><a href="#">About us</a><a href="#">Contact</a></nav>
  <div class="social social-top">meet us online <i></i><i></i></div>
</header>

<h2 class="block-title hours-title">
  <svg width="36" height="38" viewBox="0 0 36 38"><circle cx="18" cy="21" r="15" fill="none" stroke="var(--red)" stroke-width="3"/><rect x="14" y="1" width="8" height="4" fill="var(--red)"/><path d="M18 12v10h-6" fill="none" stroke="var(--red)" stroke-width="2.5"/></svg>
  Tilden's Hours
</h2>
<table class="hours">
  <tr><td>Monday - Wednesday</td><td>11 - 7</td></tr>
  <tr><td>Thursday</td><td>10:30 - 10</td></tr>
  <tr><td>Friday - Saturday</td><td>10:30 -11</td></tr>
  <tr><td>Sunday</td><td>11 - 10</td></tr>
</table>

<form class="newsletter">
  <h3>Stay in touch</h3>
  <div class="newsletter-row"><input type="text" value="Enter your email address here" aria-label="Email address"><button type="button">GO</button></div>
</form>

<h2 class="block-title location-title">
  Our Location
  <svg width="42" height="42" viewBox="0 0 42 42"><circle cx="21" cy="21" r="17" fill="#fff" stroke="var(--red)" stroke-width="3"/><path d="M21 0v6M21 36v6M0 21h6M36 21h6" stroke="var(--red)" stroke-width="2"/><path d="M29 13l-10 6 4 4z" fill="var(--red)"/><path d="M13 29l6-10 4 4z" fill="var(--ink)"/></svg>
</h2>
<address class="location" style="font-style:normal">
  4820 Cotton Gin Rd,<br>
  Millbrook TX 70512, United States<br>
  info(at)tildensbarn.example<br>
  <a href="#">Get Direction (Route Map)</a>
</address>

<section class="dishes">
  <div class="dish" style="left:98px"><span class="dish-photo" role="img" aria-label="Kebab sandwich with salad in flatbread" style="background:radial-gradient(circle at 50% 45%,#b06a2e,#6e3a16 75%)"></span><h4>Kebab Sandwich</h4><p>(Beef. Chicken. Mix)</p></div>
  <div class="dish" style="left:370px"><span class="dish-photo" role="img" aria-label="Lahmacun flatbread with a glass of ayran" style="background:radial-gradient(circle at 50% 40%,#f0d9a0,#c78a1e 75%)"></span><h4>Lahmacun</h4></div>
  <div class="dish" style="left:640px"><span class="dish-photo" role="img" aria-label="Durum wrap filled with meat and vegetables" style="background:radial-gradient(circle at 50% 50%,#e9dcc8,#a8432a 80%)"></span><h4>Durum Sandwich</h4><p>(Beef. Chicken. Mix)</p></div>
  <div class="dish" style="left:911px"><span class="dish-photo" role="img" aria-label="Kebab burger with tomato and lettuce" style="background:radial-gradient(circle at 50% 50%,#a0522d,#4b2a18 80%)"></span><h4>Kebab Special</h4></div>
</section>

<nav class="footer-nav">
  <a href="#">Home</a><a href="#">Menu</a><a href="#">Order Online</a><a href="#">Reservations</a><a href="#">Hours</a><a href="#">Location</a><a href="#">Career Openings</a><a href="#">About Us</a><a href="#">Contact</a>
</nav>
<footer class="site-footer">
  <div class="footer-brand"><span class="brand-mark"></span><span class="brand-name">Tilden's<br>Biscuit Barn</span></div>
  <div class="footer-info"><strong>Tilden's</strong><br>4820 Cotton Gin Rd, Millbrook TX 70512, United States<br>tildensbarn.example</div>
  <div class="social social-bottom">meet us online <i></i><i></i></div>
  <p class="copyright">Copyright © 2014 Tilden's &nbsp;|&nbsp; All Rights Reserved.</p>
</footer>
</body>
</html>
```